Cedar Steam & Sauna Digital Billboard

This is a digital billboard so we are looking for a fresh design that will capture people's attention. The current billboard is a simple black text "#FeelTheWarmth" over a white background with a picture of an iphone with one of our photos (Reference attached) We enjoy how clean and simple this design is, but open to other concepts. Since the weather is getting colder, a lot of people come to our spa because we offer various dry saunas and hot baths in addition to our spa services. We have a few photos for reference on our website information view www.cedarsteamhouse.com , but you can email me for additional photo content - moreno@cedarsteamhouse.com

Target Market(s)

New Jersey Locals

Colors
0255a3
ec1f27
f37122
ffc214

Requirements
Must have
• Font is "Barlow"
Nice to have
• #FeelTheWarmth hashtag

```html
<!DOCTYPE html>
<html lang="en">
<head>
<meta charset="utf-8">
<title>Cedar Steam &amp; Sauna — Billboard</title>
<link rel="stylesheet" href="https://fonts.googleapis.com/css2?family=Cinzel:wght@500&family=Poppins:wght@300;600&display=swap">
<style>
  :root {
    --backdrop: #e9eaec;
    --board: #ffffff;
    --ink: #141414;
    --ring: #5fc3cc;
    --brand-dot: #6ccad3;
    --warm-light: #f0a45a;
    --warm-mid: #b5531f;
    --warm-deep: #4a1c0c;
    --ember: #c7391d;
  }
  * { margin: 0; padding: 0; box-sizing: border-box; }
  html, body {
    width: 1200px;
    height: 880px;
    overflow: hidden;
    background: var(--backdrop);
  }
  .billboard {
    position: absolute;
    left: 40px;
    top: 276px;
    width: 1120px;
    height: 327px;
    background: var(--board);
    box-shadow: 0 14px 30px rgba(0,0,0,0.18);
  }
  .billboard svg { display: block; width: 100%; height: 100%; }
  .ring { fill: none; stroke: var(--ring); stroke-width: 2; }
  .photo { stroke: var(--board); stroke-width: 3; }
  .brand-name {
    font-family: "Cinzel", serif;
    font-weight: 500;
    fill: var(--ink);
  }
  .brand-name--main { font-size: 60px; }
  .brand-name--sub { font-size: 17px; letter-spacing: 3px; }
  .hashtag {
    font-family: "Poppins", sans-serif;
    font-size: 44px;
    font-weight: 300;
    fill: var(--ink);
  }
  .hashtag__strong { font-weight: 600; }
</style>
</head>
<body>
  <div class="billboard">
    <svg viewBox="0 0 1240 362" xmlns="http://www.w3.org/2000/svg">
      <defs>
        <radialGradient id="sauna-glow-a" cx="55%" cy="35%" r="70%">
          <stop offset="0%" stop-color="var(--warm-light)"/>
          <stop offset="60%" stop-color="var(--warm-mid)"/>
          <stop offset="100%" stop-color="var(--warm-deep)"/>
        </radialGradient>
        <radialGradient id="sauna-glow-b" cx="40%" cy="30%" r="75%">
          <stop offset="0%" stop-color="#f6c58c"/>
          <stop offset="55%" stop-color="var(--warm-light)"/>
          <stop offset="100%" stop-color="var(--warm-mid)"/>
        </radialGradient>
        <radialGradient id="sauna-glow-c" cx="25%" cy="40%" r="80%">
          <stop offset="0%" stop-color="var(--ember)"/>
          <stop offset="60%" stop-color="#6e2212"/>
          <stop offset="100%" stop-color="#2a0d07"/>
        </radialGradient>
        <radialGradient id="sauna-glow-d" cx="40%" cy="45%" r="70%">
          <stop offset="0%" stop-color="#e88a4a"/>
          <stop offset="65%" stop-color="#8a3b17"/>
          <stop offset="100%" stop-color="#3c160a"/>
        </radialGradient>
      </defs>

      <!-- decorative rings -->
      <path class="ring" d="M254,92 A137,137 0 1,0 213,326"/>
      <path class="ring" d="M313,140 A120,120 0 0,1 446,176"/>
      <path class="ring" d="M429,145 A140,140 0 0,1 677,156"/>
      <path class="ring" d="M652,200 A93,93 0 1,1 696,362"/>

      <!-- photo circles -->
      <circle class="photo" cx="166" cy="197" r="112" fill="url(#sauna-glow-a)"
              role="img" aria-label="Guest sitting cross-legged facing a glowing slatted sauna window"/>
      <circle class="photo" cx="550" cy="215" r="120" fill="url(#sauna-glow-c)"
              role="img" aria-label="Guest relaxing in a red-lit infrared sauna room"/>
      <circle class="photo" cx="712" cy="271" r="78" fill="url(#sauna-glow-d)"
              role="img" aria-label="Arched stone sauna room with a guest resting on the floor"/>
      <circle class="photo" cx="354" cy="253" r="106" fill="url(#sauna-glow-b)"
              role="img" aria-label="Three friends sitting together in a warm wooden sauna"/>

      <!-- brand -->
      <g class="brand">
        <circle cx="1021" cy="104" r="36" fill="var(--brand-dot)"/>
        <text class="brand-name brand-name--main" x="1021" y="232" text-anchor="middle">CEDAR</text>
        <text class="brand-name brand-name--sub" x="1021" y="264" text-anchor="middle">STEAM &amp; SAUNA</text>
      </g>

      <text class="hashtag" x="1021" y="324" text-anchor="middle">#FeelThe<tspan class="hashtag__strong">Warmth</tspan></text>
    </svg>
  </div>
</body>
</html>
```